Suitor Prediction Show Graphic

I need a graphic for that looks like a fancy spread sheet for a predictions game for a reality show. I want there to be 3 columns, 1:Player A, 2: Question, 3: Player B. There should be at least 10 rows. I am looking for a photoshop template that I can customize later. I have attached the graphic needed for the name of the shows as well as a very basic version of what I am looking for. Please let me know if you need additional information. It should be themed with roses and wedding rings.
SIZE:
1080px by 1920px

Font styles to use
Decorative

Colors
ec1f27
9bcb3c

Requirements
Must have
• The logo for Quelvo and Tindrel. 1080px by 1920px in size.
Nice to have
• Would be nice to have rose vines as the dividers

```html
<!DOCTYPE html>
<html lang="en">
<head>
<meta charset="utf-8">
<title>Tindrel Prediction Sheet</title>
<link rel="stylesheet" href="https://fonts.googleapis.com/css2?family=Cinzel:wght@600&family=Cinzel+Decorative:wght@400&display=swap">
<style>
  :root {
    --rose-red: #ec1f27;
    --vine-green: #9bcb3c;
    --vine-soft: #bfe3b4;
    --petal-pink: #f4b5c3;
    --petal-deep: #e48ea3;
    --ring-gold-light: #f6d77a;
    --ring-gold-dark: #c8902c;
    --ink: #2b2b2b;
    --paper: #ffffff;
  }
  * { box-sizing: border-box; margin: 0; padding: 0; }
  html, body { width: 675px; height: 1200px; overflow: hidden; background: var(--paper); }
  .sheet {
    position: relative;
    width: 675px; height: 1200px;
    padding: 8px;
    display: grid;
    grid-template-columns: 222px 1fr 222px;
    grid-template-rows: 205px repeat(10, 1fr);
    column-gap: 8px;
    background: var(--paper);
  }
  .cell {
    position: relative;
    border: 6px solid var(--vine-soft);
    outline: 2px solid var(--vine-green);
    outline-offset: -4px;
    display: flex; align-items: center; justify-content: center;
    background: var(--paper);
  }
  .rose-divider {
    position: absolute;
    top: -11px; left: 50%;
    transform: translateX(-50%);
    width: 70%; height: 20px;
    border-radius: 10px;
    background: linear-gradient(90deg, var(--vine-soft), var(--petal-pink) 25%, var(--petal-deep) 50%, var(--petal-pink) 75%, var(--vine-soft));
    z-index: 2;
  }
  .question {
    font-family: "Cinzel Decorative", serif;
    font-size: 25px;
    color: var(--ink);
    padding-top: 18px;
    white-space: nowrap;
  }
  /* header: players */
  .player { flex-direction: column; justify-content: flex-start; padding-top: 22px; gap: 4px; }
  .rings {
    width: 120px; height: 84px;
    border-radius: 50%;
    background: radial-gradient(ellipse at 40% 40%, var(--ring-gold-light), var(--ring-gold-dark));
  }
  .name-ribbon {
    width: 190px; height: 40px;
    background: var(--rose-red);
    display: flex; align-items: center; justify-content: center;
    font-family: "Cinzel", serif; font-weight: 600;
    font-size: 22px; color: var(--paper);
    letter-spacing: 1px;
  }
  /* header: show names, set as plain text */
  .branding { flex-direction: column; justify-content: flex-start; gap: 12px; }
  .crest {
    width: 150px; height: 34px;
    border-radius: 0 0 75px 75px;
    background: linear-gradient(180deg, var(--petal-deep), var(--petal-pink));
  }
  .show-name, .partner-name {
    font-family: "Cinzel Decorative", serif; font-weight: 400;
    color: var(--ink);
    line-height: 1.1;
    white-space: nowrap;
  }
  .show-name { font-size: 30px; }
  .partner-name { font-size: 22px; }
</style>
</head>
<body>
<main class="sheet">
  <section class="cell player">
    <div class="rings" role="img" aria-label="Pair of gold wedding rings"></div>
    <div class="name-ribbon">JON</div>
  </section>
  <section class="cell branding">
    <div class="crest" role="img" aria-label="Rose garland ornament"></div>
    <h1 class="show-name">Tindrel</h1>
    <p class="partner-name">Quelvo</p>
  </section>
  <section class="cell player">
    <div class="rings" role="img" aria-label="Pair of gold wedding rings"></div>
    <div class="name-ribbon">KY</div>
  </section>

  <div class="cell answer"><span class="rose-divider" role="img" aria-label="Rose vine divider"></span></div>
  <div class="cell"><span class="rose-divider" role="img" aria-label="Rose vine divider"></span><p class="question">Question 1</p></div>
  <div class="cell answer"><span class="rose-divider" role="img" aria-label="Rose vine divider"></span></div>

  <div class="cell answer"><span class="rose-divider" role="img" aria-label="Rose vine divider"></span></div>
  <div class="cell"><span class="rose-divider" role="img" aria-label="Rose vine divider"></span><p class="question">Question 2</p></div>
  <div class="cell answer"><span class="rose-divider" role="img" aria-label="Rose vine divider"></span></div>

  <div class="cell answer"><span class="rose-divider" role="img" aria-label="Rose vine divider"></span></div>
  <div class="cell"><span class="rose-divider" role="img" aria-label="Rose vine divider"></span><p class="question">Question 3</p></div>
  <div class="cell answer"><span class="rose-divider" role="img" aria-label="Rose vine divider"></span></div>

  <div class="cell answer"><span class="rose-divider" role="img" aria-label="Rose vine divider"></span></div>
  <div class="cell"><span class="rose-divider" role="img" aria-label="Rose vine divider"></span><p class="question">Question 4</p></div>
  <div class="cell answer"><span class="rose-divider" role="img" aria-label="Rose vine divider"></span></div>

  <div class="cell answer"><span class="rose-divider" role="img" aria-label="Rose vine divider"></span></div>
  <div class="cell"><span class="rose-divider" role="img" aria-label="Rose vine divider"></span><p class="question">Question 5</p></div>
  <div class="cell answer"><span class="rose-divider" role="img" aria-label="Rose vine divider"></span></div>

  <div class="cell answer"><span class="rose-divider" role="img" aria-label="Rose vine divider"></span></div>
  <div class="cell"><span class="rose-divider" role="img" aria-label="Rose vine divider"></span><p class="question">Question 6</p></div>
  <div class="cell answer"><span class="rose-divider" role="img" aria-label="Rose vine divider"></span></div>

  <div class="cell answer"><span class="rose-divider" role="img" aria-label="Rose vine divider"></span></div>
  <div class="cell"><span class="rose-divider" role="img" aria-label="Rose vine divider"></span><p class="question">Question 7</p></div>
  <div class="cell answer"><span class="rose-divider" role="img" aria-label="Rose vine divider"></span></div>

  <div class="cell answer"><span class="rose-divider" role="img" aria-label="Rose vine divider"></span></div>
  <div class="cell"><span class="rose-divider" role="img" aria-label="Rose vine divider"></span><p class="question">Question 8</p></div>
  <div class="cell answer"><span class="rose-divider" role="img" aria-label="Rose vine divider"></span></div>

  <div class="cell answer"><span class="rose-divider" role="img" aria-label="Rose vine divider"></span></div>
  <div class="cell"><span class="rose-divider" role="img" aria-label="Rose vine divider"></span><p class="question">Question 9</p></div>
  <div class="cell answer"><span class="rose-divider" role="img" aria-label="Rose vine divider"></span></div>

  <div class="cell answer"><span class="rose-divider" role="img" aria-label="Rose vine divider"></span></div>
  <div class="cell"><span class="rose-divider" role="img" aria-label="Rose vine divider"></span><p class="question">Question 10</p></div>
  <div class="cell answer"><span class="rose-divider" role="img" aria-label="Rose vine divider"></span></div>
</main>
</body>
</html>
```